Business Card Design

My company is a health food catering and delivery business. Our colours are a bright turquiose green/blue, black, white and natural brown based beige. I would like the front of my card (working from the outside in; with a turquoise green boarder -quite thick, with a thin black line separating the turquoise boarder from the beige inside the remaining space of the front of the card with my logo in the centre. This should be all that appears on the front.

On the back I would like all the information displayed above on the beige coloured card, with the blurb in the bright turquoise and my contact information in black please. I would like my business name central - Harvest Crown Kitchen and immediately below with a right alignment - ...Dine like a Monarch
Below this should follow all that I have displayed above with a left alignment.

Target Market(s)

Cafes, restaurants, individuals, buying agents & super markets

Industry/Entity Type

Catering

Contact Information for Business Card

BACK OF BUSINESS CARD:
Harvest Crown Kitchen
...Dine like a Monarch
Deliciously healthy foods - free from gluten, lactose, cane sugar, trans-fat, GMO corn, soy & rice, no artificial flavours, colours or preservatives.
Prepared fresh from locally sourced ingredients, delivered to your door! For individuals, families, corporate, cafes, restaurants & event catering for Toowoomba & surrounds!

PH: 0491 538 207 // orders@harvestcrownkitchen.example
www.harvestcrownkitchen.example
www.socialpage.example/harvestcrownkitchen

Requirements
Must have
• Please supply a modern, easy to read text that will blend nicely with my logo text.
Nice to have
• I really want my business cards to stand out as these will be the template for brochures, menus and website designers to draw inspiration from!
Should not have
• Please do not use Arial, Tahoma or Times Roman text.

```html
<!DOCTYPE html>
<html lang="en">
<head>
<meta charset="utf-8">
<title>Harvest Crown Kitchen – Business Card</title>
<link rel="stylesheet" href="https://fonts.googleapis.com/css2?family=Courgette&display=swap">
<style>
  :root {
    --turquoise: #2aa6e2;
    --ink: #111111;
    --white: #ffffff;
    --cream: #fbfaf6;
    --beige: #eddcb2;
    --stage: #e9e4dc;
    --art-tone: #e6dcc4;
  }
  * { box-sizing: border-box; margin: 0; padding: 0; }
  html, body { width: 1200px; height: 846px; overflow: hidden; }
  body {
    background: var(--stage);
    font-family: "Courgette", cursive;
    position: relative;
  }

  /* Front of card */
  .card-front {
    position: absolute;
    left: 50px; top: 40px;
    width: 680px; height: 430px;
    background: var(--white);
    border-radius: 26px;
    box-shadow: 0 6px 18px rgba(0,0,0,.18);
  }
  .front-border {
    position: absolute;
    inset: 20px;
    border: 9px solid var(--turquoise);
    border-radius: 14px;
  }
  .front-inner {
    position: absolute;
    inset: 36px;
    border: 1.5px solid var(--ink);
    border-radius: 12px;
    background: var(--cream);
  }
  .logo-art {
    position: absolute;
    left: 150px; top: 40px;
    width: 306px; height: 220px;
    background: radial-gradient(ellipse at center, var(--art-tone) 0%, var(--cream) 75%);
    border-radius: 8px;
  }
  .logo-name {
    position: absolute;
    left: 0; right: 0; top: 250px;
    text-align: center;
    font-size: 38px;
    color: var(--ink);
  }

  /* Back of card */
  .card-back {
    position: absolute;
    left: 495px; top: 380px;
    width: 645px; height: 430px;
    background: var(--beige);
    border-radius: 26px;
    box-shadow: 0 6px 18px rgba(0,0,0,.2);
    padding: 44px 48px 0 50px;
  }
  .blurb {
    color: var(--turquoise);
    font-size: 16.5px;
    line-height: 1.45;
  }
  .business-name {
    margin-top: 20px;
    text-align: center;
    color: var(--turquoise);
    font-size: 29px;
    font-weight: 400;
    line-height: 1.1;
  }
  .tagline {
    text-align: right;
    padding-right: 120px;
    color: var(--turquoise);
    font-size: 15px;
    line-height: 1;
  }
  .contact {
    position: absolute;
    left: 34px; right: 18px; top: 318px;
    display: flex;
    color: var(--ink);
  }
  .contact-col { display: flex; flex-direction: column; gap: 14px; padding: 6px 0; }
  .contact-col.primary { width: 268px; flex: none; padding-right: 10px; }
  .contact-col.online { border-left: 1.5px solid var(--ink); padding-left: 18px; }
  .contact-item { display: flex; align-items: center; gap: 10px; white-space: nowrap; font-size: 13.5px; }
  .contact-item.phone { font-size: 16.5px; letter-spacing: .5px; }
  .contact-col.online .contact-item { font-size: 12.5px; }
  .icon { width: 16px; height: 16px; flex: none; }
</style>
</head>
<body>

<section class="card-front" aria-label="Front of business card">
  <div class="front-border"></div>
  <div class="front-inner">
    <div class="logo-art" role="img" aria-label="Logo illustration: a chef in a tall hat and apron holding a whisk and a frying pan"></div>
    <div class="logo-name">Harvest Crown Kitchen</div>
  </div>
</section>

<section class="card-back" aria-label="Back of business card">
  <p class="blurb">Deliciously healthy foods - free from gluten, lactose, cane sugar, trans-fat, GMO corn, soy &amp; rice, no artificial flavours, colours or preservatives. Prepared fresh from locally sourced ingredients, delivered to your door! For individuals, families, corporate, cafes, restaurants &amp; event catering for Toowoomba &amp; surrounds!</p>
  <h1 class="business-name">Harvest Crown Kitchen</h1>
  <p class="tagline">...Dine like a Monarch</p>

  <div class="contact">
    <div class="contact-col primary">
      <div class="contact-item phone">
        <svg class="icon" viewBox="0 0 16 16" aria-hidden="true"><rect width="16" height="16" rx="2" fill="var(--ink)"/><path d="M4.5 3.5l2 .3.6 2.4-1.3.9a6 6 0 0 0 3.1 3.1l.9-1.3 2.4.6.3 2a1.3 1.3 0 0 1-1.4 1A8.5 8.5 0 0 1 3.5 4.9a1.3 1.3 0 0 1 1-1.4z" fill="var(--beige)"/></svg>
        0491 538 207
      </div>
      <div class="contact-item">
        <svg class="icon" viewBox="0 0 16 16" aria-hidden="true"><rect x="1" y="3" width="14" height="10" rx="1" fill="none" stroke="var(--ink)" stroke-width="1.6"/><path d="M1.5 3.8L8 9l6.5-5.2" fill="none" stroke="var(--ink)" stroke-width="1.6"/></svg>
        orders@harvestcrownkitchen.example
      </div>
    </div>
    <div class="contact-col online">
      <div class="contact-item">
        <svg class="icon" viewBox="0 0 16 16" aria-hidden="true"><rect width="16" height="16" rx="2" fill="var(--ink)"/></svg>
        www.socialpage.example/harvestcrownkitchen
      </div>
      <div class="contact-item">
        <svg class="icon" viewBox="0 0 16 16" aria-hidden="true"><rect width="16" height="16" rx="2" fill="var(--ink)"/><circle cx="8" cy="8" r="5" fill="none" stroke="var(--beige)" stroke-width="1.2"/><ellipse cx="8" cy="8" rx="2.2" ry="5" fill="none" stroke="var(--beige)" stroke-width="1.1"/><path d="M3 8h10" stroke="var(--beige)" stroke-width="1.1"/></svg>
        www.harvestcrownkitchen.example
      </div>
    </div>
  </div>
</section>

</body>
</html>
```